Job Posting for Licensed Veterinary Technician

We would like an eye catching job posting that we can send to technician schools in order to recruit veterinary technicians (LVTs) to our veterinary hospital

```html
<!DOCTYPE html>
<html lang="en">
<head>
<meta charset="utf-8">
<title>Job Posting – Licensed Veterinary Technician</title>
<link href="https://fonts.googleapis.com/css2?family=Montserrat:wght@400;500;600;700;800&display=swap" rel="stylesheet">
<style>
:root{
  --green:#3b6d3a;
  --teal:#1b96b0;
  --ink:#222222;
  --white:#ffffff;
  --page-bg:#f2f2f2;
  --seal:#d9dde0;
  --paw:#8cc63f;
}
*{margin:0;padding:0;box-sizing:border-box}
html,body{width:783px;height:1200px;overflow:hidden;background:var(--page-bg);font-family:'Montserrat',sans-serif;color:var(--ink)}
.poster{position:absolute;left:0;top:46px;width:725px;height:1025px;background:var(--white);transform:scale(1.08);transform-origin:0 0;overflow:hidden;box-shadow:0 2px 10px rgba(0,0,0,.15)}
.abs{position:absolute}

/* brand */
.brand{left:50px;top:55px;display:flex;align-items:center;gap:10px}
.brand-dot{width:56px;height:56px;border-radius:50%;background:var(--teal)}
.brand-name{font-weight:600;font-size:21px;line-height:1.05;color:var(--green)}

/* headline */
.headline{left:55px;top:130px;font-weight:800;line-height:1}
.headline .l-green{font-size:35px;color:var(--green);display:block}
.headline .l-sub{font-size:21px;font-weight:400;color:var(--ink);display:block;margin:3px 0 4px}
.headline .l-teal{font-size:35px;color:var(--teal);display:block}
.rule{height:3px;width:57px;background:var(--green)}
.rule.white{background:var(--white);width:28px;height:2px}
.rule.short{width:28px;height:2px}

.photo{left:360px;top:30px;width:365px;height:290px;background:radial-gradient(ellipse at 45% 55%,#c89a6c 0%,#e8d8c6 45%,#ffffff 75%)}
.waves{left:0;top:0}

/* description */
.desc-title{left:0;top:368px;width:725px;text-align:center;color:var(--white);font-weight:800;font-size:18px;display:flex;justify-content:center;align-items:center;gap:8px}
.desc{left:58px;top:413px;width:610px;color:var(--white);font-size:9.4px;line-height:1.22;text-align:center}
.desc p{margin-bottom:13px}

/* lists */
.sec-title{font-weight:700;font-size:12.5px;color:var(--teal);line-height:1.25}
.sec-title span{color:var(--ink);display:block}
.duties{left:44px;top:577px}
.quals{left:44px;top:816px}
.checklist{list-style:none;font-size:9.6px;font-weight:600;line-height:1.12}
.checklist li{position:absolute;padding-left:19px;width:160px}
.checklist li::before{content:"";position:absolute;left:0;top:1px;width:10px;height:10px;border-radius:50%;background:var(--teal)}
.checklist li::after{content:"";position:absolute;left:3.4px;top:2.6px;width:2.5px;height:5px;border:solid var(--white);border-width:0 1.4px 1.4px 0;transform:rotate(45deg)}

/* offer */
.offer{left:392px;top:574px;width:299px;height:174px;border-radius:8px;background:var(--teal);color:var(--white);padding:24px 25px 0 29px}
.offer h2{font-size:17px;font-weight:700;margin-bottom:9px}
.offer p{font-size:9.4px;line-height:1.18;text-align:justify;margin-top:14px}

.job{font-weight:700;font-size:12.5px;color:var(--teal)}
.job b{color:var(--ink)}
.note{left:392px;top:800px;width:280px;font-size:9px;line-height:1.2}
.seal{left:392px;top:878px;width:50px;height:50px;border-radius:50%;background:var(--seal)}
.mascot{left:585px;top:878px;width:140px;height:120px;background:radial-gradient(ellipse at center,#d8d8d8 0%,#ffffff 70%)}

/* footer */
.footer-text{color:var(--white);font-weight:700;font-size:17px;display:flex;align-items:center;gap:6px}
.web{left:508px;top:983px;font-weight:700;font-size:12.5px;letter-spacing:.3px}
</style>
</head>
<body>
<div class="poster">

  <div class="abs photo" role="img" aria-label="Photo of a smiling collie dog and a calico cat sitting side by side, cradled by a stylised hand"></div>

  <svg class="abs waves" width="725" height="1025" viewBox="0 0 725 1025" aria-hidden="true">
    <path d="M0 305 C180 330 320 345 420 345 C540 345 640 310 725 295 L725 553 L0 553 Z" fill="var(--green)"/>
    <path d="M0 272 C140 305 270 330 400 335 C520 338 630 300 725 262 L725 295 C640 312 540 347 420 347 C300 345 150 325 0 305 Z" fill="var(--teal)"/>
    <path d="M0 305 C150 320 280 337 400 342" stroke="var(--white)" stroke-width="2" fill="none"/>
    <path d="M0 952 L450 952 C475 952 478 985 485 1000 L725 1000 L725 1025 L0 1025 Z" fill="var(--green)"/>
    <rect x="485" y="1000" width="240" height="8" fill="var(--teal)"/>
  </svg>

  <div class="abs brand">
    <div class="brand-dot"></div>
    <div class="brand-name">Harbor Lane<br>Animal Clinic</div>
  </div>

  <h1 class="abs headline">
    <span class="l-green">JOB POSTING</span>
    <span class="l-sub">FOR LICENSED</span>
    <span class="l-teal">VETERINARY</span>
    <span class="l-teal">TECHNICIAN</span>
    <span class="rule" style="display:block;margin-top:8px"></span>
  </h1>

  <h2 class="abs desc-title">
    <svg width="13" height="12" viewBox="0 0 13 12" aria-hidden="true"><g fill="var(--paw)"><ellipse cx="6.5" cy="8.5" rx="3.2" ry="2.7"/><circle cx="2" cy="5" r="1.4"/><circle cx="4.5" cy="2" r="1.4"/><circle cx="8.5" cy="2" r="1.4"/><circle cx="11" cy="5" r="1.4"/></g></svg>
    JOB DESCRIPTION
    <svg width="13" height="12" viewBox="0 0 13 12" aria-hidden="true"><g fill="var(--paw)"><ellipse cx="6.5" cy="8.5" rx="3.2" ry="2.7"/><circle cx="2" cy="5" r="1.4"/><circle cx="4.5" cy="2" r="1.4"/><circle cx="8.5" cy="2" r="1.4"/><circle cx="11" cy="5" r="1.4"/></g></svg>
  </h2>

  <div class="abs desc">
    <p>Harbor Lane Animal Clinic (412 Bayview Avenue in Norfolk) is growing and excited to announce an opening for a part- or full-time Licensed Veterinary Technician. Our new Hospital opened in late 2015 and is a full service medical, dental and surgical center with a focus on preventive medicine. We are also equipped and able to handle most daytime emergency cases.</p>
    <p>Applicants must be energetic, compassionate, welcoming, positive, and enjoy interfacing with both clients and pets. An extraordinary attention to detail in caring for our clients' and patients' needs is a must. We are a paperless facility, and expertise in electronic medical records or the ability to quickly learn these systems is required.</p>
    <p>Harbor Lane Animal Clinic is AVQA-Accredited, and our medical staff are all Calm Care Certified. We are located in the historic Larchmont neighborhood of Norfolk, minutes from Downtown Norfolk and the beaches of Norfolk and Virginia Beach.</p>
  </div>

  <div class="abs duties">
    <h3 class="sec-title">YOU DUTIES MAY INCLUDE,<span>BUT ARE NOT LIMITED TO</span></h3>
    <div class="rule short" style="margin-top:6px"></div>
  </div>

  <ul class="abs checklist" style="left:44px;top:0">
    <li style="top:637px">Ensure the best possible client/ patient experience</li>
    <li style="top:668px">Take digital radiographs</li>
    <li style="top:688px">Venapuncture</li>
    <li style="top:709px">IV catheter placement</li>
    <li style="top:729px">Blood pressure monitoring</li>
    <li style="top:750px">Induction and monitoring of anesthesia</li>
    <li style="top:781px">Administration and logging of controlled medications</li>
    <li style="top:637px;left:173px">Run/Process lab work</li>
    <li style="top:659px;left:173px">Assist and monitor in surgery</li>
    <li style="top:692px;left:173px">Educate clients</li>
    <li style="top:715px;left:173px">Discharge patients</li>
    <li style="top:737px;left:173px">Share ideas</li>
    <li style="top:759px;left:173px">Discuss cases</li>
    <li style="top:781px;left:173px">Medicate and restrain patients</li>

    <li style="top:858px">LVT, licensed to practice in the Commonwealth of Virginia</li>
    <li style="top:900px">Excellent people skills</li>
    <li style="top:922px">Team player</li>
    <li style="top:858px;left:173px">Proficient in technical skills and excited to use them</li>
    <li style="top:906px;left:173px">Ability to complete above duties</li>
  </ul>

  <div class="abs quals">
    <h3 class="sec-title">QUALIFICATIONS</h3>
    <div class="rule short" style="margin-top:6px"></div>
  </div>

  <section class="abs offer">
    <h2>WE OFFER</h2>
    <div class="rule white"></div>
    <p>Very competitive compensation based on skills and experience Employer-sponsored retirement plan with matching contributions Short and long term disability insurance (100% employer paid for FT) Medical insurance (employer contributions for FT) Life insurance (100% employer paid for FT) Employee discounts Vacation time and holiday pay for full time employees</p>
  </section>

  <div class="abs" style="left:392px;top:767px">
    <p class="job">JOB TYPE: <b>FULL-TIME</b></p>
    <div class="rule short" style="margin-top:6px"></div>
  </div>
  <p class="abs note">* Only applicants who apply through this posting will be considered. NO in-person applicants will be considered *</p>
  <div class="abs" style="left:392px;top:839px">
    <p class="job">JOB TYPES: <b>FULL-TIME, PART-TIME</b></p>
    <div class="rule short" style="margin-top:6px"></div>
  </div>

  <div class="abs seal" role="img" aria-label="Accreditation seal"></div>
  <div class="abs mascot" role="img" aria-label="Line illustration of a cartoon dog on a leash"></div>

  <div class="abs footer-text" style="left:48px;top:976px">
    <svg width="13" height="13" viewBox="0 0 24 24" aria-hidden="true"><path fill="none" stroke="#fff" stroke-width="2.4" d="M6.6 2.5l3 3.6-1.9 2.3c1.3 2.9 3.6 5.3 6.5 6.6l2.3-1.9 3.6 3-1.8 3.4C11 18.8 5.2 13 4.2 4.3z"/></svg>
    757-555-0142
  </div>
  <div class="abs footer-text" style="left:210px;top:976px;font-size:14.5px">
    <svg width="15" height="11" viewBox="0 0 15 11" aria-hidden="true"><rect x=".8" y=".8" width="13.4" height="9.4" fill="none" stroke="#fff" stroke-width="1.5"/><path d="M1 1l6.5 5 6.5-5M1 10l5-4M14 10l-5-4" fill="none" stroke="#fff" stroke-width="1.3"/></svg>
    hello@harborlanevet.com
  </div>
  <p class="abs web">www.harborlanevet.com</p>

</div>
</body>
</html>
```